Tri-fold Brochure Design for New Custom Home Model

We need an expert to design a tri-fold brochure to showcase our new custom home model.<br/>The concept is as follow:<br/>We are introducing a fixed prize affordable custom home. We are trying to target landowners or homeowners who would like to build a custom home. We have a fixed design for exterior, interior. 3 level layout. Basement, main level, first floor.<br/>We have hand-drew the desired layout as you can see in the document attached names "hand-drawing". We would like the design to follow that idea.<br/>The required photos and info are attached. Please check out the attached documents here.<br/> The text content, material details can be found in the PDF file attached.

Target Market(s)

Home Owner, Land-owner, people who wants to build a new home

Industry/Entity Type

Residential Construction

Font styles to use
Sans Serif

Colors
ec1f27
fffefd

Requirements
Must have
• Formal text language, attractive design
Nice to have
• Most attractive and lead generating design
Should not have
• more than two colours, flashy design.

```html
<!DOCTYPE html>
<html lang="en">
<head>
<meta charset="utf-8">
<title>Custom Home Model – Tri-fold Brochure</title>
<link href="https://fonts.googleapis.com/css2?family=Montserrat:wght@700;800&family=Roboto:wght@400;500;700&family=Roboto+Condensed:wght@400;700&display=swap" rel="stylesheet">
<style>
:root{
  --blue:#28467a;
  --blue-dark:#1f3a68;
  --red:#ec1f27;
  --paper:#fffefd;
  --ink:#222;
  --stage:#5b5b5b;
  --plan-wall:#d9a46e;
  --plan-glass:#c9e0e2;
}
*{box-sizing:border-box;margin:0;padding:0}
html,body{width:1200px;height:1200px;overflow:hidden;background:var(--stage);font-family:'Roboto',sans-serif;color:var(--ink)}
.sheet{position:absolute;left:248px;width:683px;height:529px;background:var(--paper);overflow:hidden}
.sheet--outside{top:62px}
.sheet--inside{top:616px}
.panel{position:absolute;top:0;height:529px}
.p1{left:0;width:224px}
.p2{left:224px;width:226px;background:linear-gradient(90deg,#e9ebee,#fafafa 40%,#f3f4f6)}
.p3{left:450px;width:233px;background:linear-gradient(90deg,#e6e8eb,#fafafa 30%)}
.abs{position:absolute}
.bar{position:absolute;bottom:0;height:7px;width:180px}
.bar--red{background:var(--red)}
.bar--blue{background:var(--blue)}
.photo{position:absolute}

/* About */
.about{left:0;top:223px;width:213px;height:169px;background:var(--blue);color:#fff;padding:15px 13px 0 12px}
.about h2{font-family:'Montserrat',sans-serif;font-weight:800;font-size:19px;letter-spacing:.3px}
.about .rule{width:18px;height:3px;background:#fff;margin:6px 0 14px}
.about p{font-size:8.3px;line-height:10.3px;text-align:justify}
.ribbon{left:42px;top:381px;width:134px;height:22px;background:var(--red);color:#fff;font-family:'Roboto Condensed',sans-serif;font-size:14px;text-align:center;line-height:22px;clip-path:polygon(6% 0,100% 0,94% 100%,0 100%)}
.badge{position:absolute;background:#e4e6ea;border-radius:3px}

/* Why us */
.why{left:11px;top:0;width:206px;height:221px;background:var(--blue);color:#fff}
.why-label{position:absolute;left:49px;top:22px;width:115px;height:21px;background:#fff;color:var(--red);font-family:'Montserrat',sans-serif;font-weight:800;font-size:15px;text-align:center;line-height:21px}
.why-grid{position:absolute;left:9px;top:62px;width:188px;display:grid;grid-template-columns:repeat(3,1fr);grid-template-rows:72px 82px}
.why-item{display:flex;flex-direction:column;align-items:center;font-size:8.5px;text-align:center;line-height:10px;padding-top:6px}
.why-item svg{width:22px;height:22px;margin-bottom:6px}
.why-item:nth-child(1),.why-item:nth-child(2),.why-item:nth-child(4),.why-item:nth-child(5){border-right:1px dashed rgba(255,255,255,.6)}
.why-item:nth-child(-n+3){border-bottom:1px dashed rgba(255,255,255,.6)}
.why-item:nth-child(n+4){padding-top:14px}

.brand{font-family:'Montserrat',sans-serif;font-weight:800;color:var(--blue);display:flex;align-items:center;gap:6px;line-height:1}
.brand .dot{border-radius:50%;background:var(--blue);flex:none}
.contact{position:absolute;left:0;width:226px;text-align:center;font-size:8.3px}
.contact svg{width:12px;height:12px;display:block;margin:0 auto 6px}
.contact b{font-weight:700;display:block}

/* Cover */
.price{left:108px;top:221px;width:125px;height:69px;background:var(--red);color:#fff;text-align:center;padding-top:4px}
.price .amt{font-family:'Roboto Condensed',sans-serif;font-weight:700;font-size:31px;line-height:32px}
.price .amt sup{font-size:13px;vertical-align:12px}
.price .l1{font-family:'Roboto Condensed',sans-serif;font-size:11.5px;line-height:11px}
.price .l2{font-family:'Montserrat',sans-serif;font-weight:800;font-size:13.5px;line-height:15px}
.cta{left:12px;top:390px;width:221px;height:97px;background:var(--blue);color:#fff;text-align:center;padding-top:10px}
.cta .s1{font-size:14.5px}
.cta .s2{font-family:'Roboto',sans-serif;font-weight:500;font-size:16.5px;margin-top:1px}
.cta .phone{display:flex;align-items:center;justify-content:center;gap:10px;margin-top:7px;font-size:21px}
.cta .phone span.ic{width:35px;height:35px;border-radius:50%;background:#fff;display:flex;align-items:center;justify-content:center}
.web{font-size:8.3px;text-align:center;width:233px;left:0}

/* Inside */
.lvl-head{position:absolute;top:0;left:0;right:0;height:32px;color:#fff;font-family:'Montserrat',sans-serif;font-weight:800;font-size:15px;text-align:center;line-height:34px;letter-spacing:.3px}
.lvl-head--blue{background:var(--blue)}
.lvl-head--red{background:var(--red)}
.lvl{background:linear-gradient(90deg,#eceef1,#fafafa 30%)}
.lvl-photo{left:8px;right:8px;top:32px;height:96px}
.plan{left:10px;top:134px;width:128px;height:180px;border:1px solid #c9ccd1;
  background:
    radial-gradient(ellipse 58% 52% at 50% 52%,rgba(217,164,110,.55),rgba(217,164,110,.22) 60%,rgba(255,255,255,0) 80%),
    linear-gradient(180deg,#fbfbfb,#f1f2f4);}
.plan--upper{width:130px;
  background:
    radial-gradient(ellipse 55% 45% at 50% 42%,rgba(217,164,110,.55),rgba(217,164,110,.2) 60%,rgba(255,255,255,0) 80%),
    linear-gradient(180deg,#fbfbfb 60%,var(--plan-glass));}
.vtext{position:absolute;writing-mode:vertical-rl;transform:rotate(180deg);font-size:8.5px;white-space:nowrap;font-weight:500}
.vline{position:absolute;width:1px;background:#555}
.sheetno{position:absolute;width:16px;height:16px;border:1px solid #555;border-radius:50%;font-size:7px;text-align:center;line-height:14px;background:#fff}
.fin-title{position:absolute;left:14px;top:332px;border-left:3px solid var(--blue);padding-left:4px;color:var(--red);font-weight:700;font-size:10.5px;line-height:12px}
.swatches{position:absolute;top:352px;width:88px;height:71px;border:1px solid #c9ccd1;background:#fff;padding:3px}
.sw{display:flex;gap:5px;align-items:flex-start;height:32px;margin-bottom:1px}
.sw i{display:block;width:32px;height:31px;flex:none}
.sw span{font-size:3.6px;line-height:4.4px;color:#444;text-decoration:underline;padding-top:4px}
.tb{position:absolute;left:12px;top:434px;width:200px;height:35px;border:1px solid #777;display:grid;grid-template-columns:60px 56px 42px 1fr;font-size:8.3px;background:#fff}
.tb div{padding:4px 0 0 5px;line-height:15px;border-right:1px solid #777}
.tb div:last-child{border-right:none}
.rev{position:absolute;left:14px;top:480px;width:198px;font-size:8.3px}
.rev span{position:absolute}
.rev i{position:absolute;top:21px;height:1px;background:#999}
</style>
</head>
<body>

<section class="sheet sheet--outside">
  <div class="panel p1">
    <div class="photo" style="left:0;top:0;width:224px;height:223px;background:linear-gradient(160deg,#cfc8bb,#9c8f7d 55%,#6b5b49)" role="img" aria-label="Interior render of an open kitchen with bar stools and dining area"></div>
    <div class="abs about">
      <h2>ABOUT US</h2>
      <div class="rule"></div>
      <p>At Northshore Custom Builders we specialize in home renovations and custom home builds throughout the Greater Coastview and Lower Mainland area. Our mission is to provide our clients with a seamless experience. An experience that transforms their home into beautiful functional art that reflects the lifestyle they choose to lead.</p>
    </div>
    <div class="abs ribbon">Our Credentials</div>
    <div class="badge" style="left:21px;top:429px;width:38px;height:22px"></div>
    <div class="badge" style="left:80px;top:417px;width:30px;height:32px"></div>
    <div class="badge" style="left:123px;top:421px;width:34px;height:30px"></div>
    <div class="badge" style="left:168px;top:421px;width:40px;height:28px"></div>
    <div class="badge" style="left:78px;top:467px;width:28px;height:36px"></div>
    <div class="badge" style="left:125px;top:478px;width:30px;height:26px"></div>
    <div class="bar bar--red" style="left:20px"></div>
  </div>

  <div class="panel p2">
    <div class="abs why">
      <div class="why-label">WHY US?</div>
      <div class="why-grid">
        <div class="why-item"><svg viewBox="0 0 24 24" fill="#fff"><path d="M12 2 2 7v2h20V7z"/><rect x="4" y="10" width="2.5" height="8"/><rect x="8.5" y="10" width="2.5" height="8"/><rect x="13" y="10" width="2.5" height="8"/><rect x="17.5" y="10" width="2.5" height="8"/><rect x="2" y="19" width="20" height="3"/></svg>In-House<br>Financing</div>
        <div class="why-item"><svg viewBox="0 0 24 24" fill="#fff"><circle cx="12" cy="7" r="5"/><path d="M3 23c0-6 4-9 9-9s9 3 9 9z"/></svg>Managment</div>
        <div class="why-item"><svg viewBox="0 0 24 24" fill="#fff"><path d="M7 11V8a5 5 0 0 1 10 0v3h-2.5V8a2.5 2.5 0 0 0-5 0v3z"/><rect x="4" y="11" width="16" height="11" rx="1.5"/></svg>Warranty</div>
        <div class="why-item"><svg viewBox="0 0 24 24" fill="#fff"><path d="M21 2c1 1-7 11-9 12l-2-2C11 10 20 1 21 2z"/><path d="M8 14c-3 0-5 2-5 5 0 1-1 2-2 2 3 2 9 1 9-4z"/></svg>Design</div>
        <div class="why-item"><svg viewBox="0 0 24 24" fill="none" stroke="#fff" stroke-width="2" stroke-linejoin="round"><path d="M1 8l5-3 6 4 6-4 5 3v6l-5 2-4 4-3-1-6-5-4-1z"/><path d="M9 11l3 2 3-2"/></svg>Honesty</div>
        <div class="why-item"><svg viewBox="0 0 24 24" fill="none" stroke="#fff" stroke-width="2"><rect x="2" y="5" width="20" height="14" rx="1"/><circle cx="12" cy="12" r="3.5" fill="#fff"/></svg>Affordable<br>Pricing</div>
      </div>
    </div>
    <div class="abs brand" style="left:50px;top:262px;font-size:13px"><span class="dot" style="width:22px;height:22px"></span><span>NORTHSHORE<br>CUSTOM BUILDERS</span></div>
    <div class="contact" style="top:323px"><svg viewBox="0 0 24 24" fill="var(--red)"><path d="M12 1a8 8 0 0 0-8 8c0 6 8 14 8 14s8-8 8-14a8 8 0 0 0-8-8zm0 11a3 3 0 1 1 0-6 3 3 0 0 1 0 6z"/></svg><b>Northshore Custom Builders</b>410-2275 Harbour Street, Coastview, BC V0X 2A1</div>
    <div class="contact" style="top:390px"><svg viewBox="0 0 24 24" fill="var(--red)"><path d="M2 5h20v14H2z"/><path d="M2 5l10 8 10-8" stroke="#fff" stroke-width="1.8" fill="none"/></svg>info@northshorecustombuilders.com</div>
    <div class="contact" style="top:433px"><svg viewBox="0 0 24 24" fill="var(--red)"><path d="M7 2c1 0 3 4 3 5s-2 2-2 3 3 6 5 7c1 0 2-2 3-2s5 2 5 3-2 4-4 4C9 22 2 13 2 7c0-2 3-5 5-5z"/></svg>(555) 210 4870</div>
    <div class="contact" style="top:482px"><svg viewBox="0 0 24 24" fill="none" stroke="var(--red)" stroke-width="2"><circle cx="12" cy="12" r="10"/><ellipse cx="12" cy="12" rx="4" ry="10"/><path d="M2 12h20"/></svg>www.northshorecustombuilders.com</div>
    <div class="bar bar--blue" style="left:24px"></div>
  </div>

  <div class="panel p3">
    <div class="abs brand" style="left:32px;top:24px;font-size:15px"><span class="dot" style="width:28px;height:28px"></span><span>NORTHSHORE<br>CUSTOM BUILDERS</span></div>
    <div class="photo" style="left:12px;top:76px;width:221px;height:182px;background:linear-gradient(180deg,#cfe0ef,#6f7f93 45%,#5a6a7e)" role="img" aria-label="Exterior render of the two-storey model home with grey siding and shingled gables"></div>
    <div class="photo" style="left:12px;top:262px;width:221px;height:126px;background:linear-gradient(180deg,#d6e4f0,#7b8a9c 50%,#9aa2aa)" role="img" aria-label="Exterior render of the home's side with a garage"></div>
    <div class="abs price"><div class="amt"><sup>$</sup>549,000</div><div class="l1">THIS COULD BE</div><div class="l2">YOUR HOME</div></div>
    <div class="abs cta">
      <div class="s1">Also earn 1500/m</div>
      <div class="s2">CALL US &amp; ASK HOW?</div>
      <div class="phone"><span class="ic"><svg width="20" height="20" viewBox="0 0 24 24" fill="var(--red)"><path d="M7 2c1 0 3 4 3 5s-2 2-2 3 3 6 5 7c1 0 2-2 3-2s5 2 5 3-2 4-4 4C9 22 2 13 2 7c0-2 3-5 5-5z"/></svg></span>(555) 210 4870</div>
    </div>
    <div class="abs web" style="top:496px">www.northshorecustombuilders.com</div>
    <div class="bar bar--red" style="left:28px"></div>
  </div>
</section>

<section class="sheet sheet--inside">
  <div class="panel lvl" style="left:0;width:225px">
    <div class="lvl-head lvl-head--blue">BASEMENT LEVEL</div>
    <div class="photo lvl-photo" style="background:linear-gradient(180deg,#e6e2dc,#c9bfb2 60%,#a08a6e)" role="img" aria-label="Basement lounge render with fireplace and sofa"></div>
    <div class="photo plan" role="img" aria-label="Basement floor finishes plan: unfinished basement, two bedrooms, bath, utility and entry"></div>
    <div class="vtext" style="left:156px;top:208px">TOTAL AREA: 959.58 SF</div>
    <div class="vtext" style="left:182px;top:148px;font-weight:700">0 BASEMENT FLOOR - FINISHES PLAN</div>
    <div class="vline" style="left:195px;top:140px;height:162px"></div>
    <div class="vtext" style="left:201px;top:252px">3/16" = 1'-0"</div>
    <div class="sheetno" style="left:190px;top:302px">1</div>
    <div class="fin-title">BASEMENT FINISHES</div>
    <div class="swatches" style="left:12px">
      <div class="sw"><i style="background:#b9b1a6"></i><span>FL1 Laminate Floor Oak</span></div>
      <div class="sw"><i style="background:#a8997f"></i><span>FL2 Carpet Sand Stone</span></div>
    </div>
    <div class="swatches" style="left:125px">
      <div class="sw"><i style="background:#bdb5aa"></i><span>TL1 Porcelain Tile</span></div>
      <div class="sw"><i style="background:#d2d4d2"></i><span>Grout Frost</span></div>
    </div>
    <div class="tb"><div>Scale @ A3<br>3/16" = 1'-0"</div><div>Date<br>01-29-2020</div><div>Drawn<br>DC</div><div>Dwg. no<br>SK1.1</div></div>
    <div class="rev"><span style="left:0">Rev.</span><span style="left:62px">Date</span><span style="left:125px">Description</span><i style="left:0;width:55px"></i><i style="left:62px;width:56px"></i><i style="left:125px;width:73px"></i></div>
    <div class="bar bar--red" style="left:20px"></div>
  </div>

  <div class="panel lvl" style="left:225px;width:225px">
    <div class="lvl-head lvl-head--red">MAIN LEVEL</div>
    <div class="photo lvl-photo" style="background:linear-gradient(180deg,#e4e5e6,#bfc0bf 60%,#5a5a5c)" role="img" aria-label="Main level living room render with stairs and sofa"></div>
    <div class="photo plan" role="img" aria-label="Main floor finishes plan: family room, kitchen, dining room, living room and entry porch"></div>
    <div class="vtext" style="left:156px;top:203px">TOTAL AREA: 946.36 SF</div>
    <div class="vtext" style="left:182px;top:166px;font-weight:700">1 MAIN FLOOR - FINISHES PLAN</div>
    <div class="vline" style="left:195px;top:140px;height:162px"></div>
    <div class="vtext" style="left:201px;top:247px">3/16" = 1'-0"</div>
    <div class="sheetno" style="left:186px;top:298px">1</div>
    <div class="fin-title">MAIN FLOOR FINISHES</div>
    <div class="swatches" style="left:12px">
      <div class="sw"><i style="background:#b9b1a6"></i><span>FL1 Laminate Floor Oak</span></div>
      <div class="sw"><i style="background:#a8997f"></i><span>FL2 Carpet Sand Stone</span></div>
    </div>
    <div class="swatches" style="left:125px">
      <div class="sw"><i style="background:#bdb5aa"></i><span>TL1 Porcelain Tile</span></div>
      <div class="sw"><i style="background:#d2d4d2"></i><span>Grout Frost</span></div>
    </div>
    <div class="tb"><div>Scale @ A3<br>3/16" = 1'-0"</div><div>Date<br>01-29-2020</div><div>Drawn<br>DC</div><div>Dwg. no<br>SK2.1</div></div>
    <div class="rev"><span style="left:0">Rev.</span><span style="left:64px">Date</span><span style="left:127px">Description</span><i style="left:0;width:57px"></i><i style="left:64px;width:56px"></i><i style="left:127px;width:71px"></i></div>
    <div class="bar bar--blue" style="left:24px"></div>
  </div>

  <div class="panel lvl" style="left:450px;width:233px">
    <div class="lvl-head lvl-head--blue">UPPER FLOOR</div>
    <div class="photo lvl-photo" style="left:7px;background:linear-gradient(160deg,#bdb8b2,#d8d4ce 55%,#c6ac86)" role="img" aria-label="Upper floor bathroom render with vanity and mirror"></div>
    <div class="photo plan plan--upper" role="img" aria-label="Upper floor finishes plan: master bedroom, two bedrooms, baths, laundry and roof below"></div>
    <div class="vtext" style="left:160px;top:200px">TOTAL AREA: 804.27 SF</div>
    <div class="vtext" style="left:186px;top:166px;font-weight:700">2 MAIN FLOOR - FINISHES PLAN</div>
    <div class="vline" style="left:199px;top:140px;height:162px"></div>
    <div class="vtext" style="left:205px;top:247px">3/16" = 1'-0"</div>
    <div class="sheetno" style="left:186px;top:298px">1</div>
    <div class="fin-title">UPPER FLOOR FINISHES</div>
    <div class="swatches" style="left:13px">
      <div class="sw"><i style="background:#a8997f"></i><span>FL2 Carpet Sand Stone</span></div>
      <div class="sw"><i style="background:#bdb5aa"></i><span>TL1 Porcelain Tile</span></div>
    </div>
    <div class="swatches" style="left:125px;height:40px">
      <div class="sw"><i style="background:#d2d4d2"></i><span>Grout Frost</span></div>
    </div>
    <div class="tb" style="left:13px"><div>Scale @ A3<br>3/16" = 1'-0"</div><div>Date<br>01-29-2020</div><div>Drawn<br>DC</div><div>Dwg. no<br>SK3.1</div></div>
    <div class="rev" style="left:15px"><span style="left:0">Rev.</span><span style="left:63px">Date</span><span style="left:126px">Description</span><i style="left:0;width:56px"></i><i style="left:63px;width:56px"></i><i style="left:126px;width:72px"></i></div>
    <div class="bar bar--red" style="left:28px"></div>
  </div>
</section>

</body>
</html>
```